Protein Powder Product Label Design

We are going to launch Protein Powder Product shortly and looking for the Unique, Attractive and Best Product label Design. The label size should be 5.5x17.

Here are some competitors label design which I like the most:
https://trelquo.com/collections/daily-nutrition/products/dorn-pax-organic?variant=48201937561420 (Like the way it described each nutrition element at the bottom & Flavors Image)
https://www.quimbrix.com/products/calmrise-stress-anxiety-relief (Like the Logo on Side)
www.7xq.ord (Overall Designs & Color Combination)

I have attached Generic Product Label design template so that you can have all the content required for the label.

Target Market(s)

Nutrition, Sport Nutrition, Protein Powder

Industry/Entity Type

Nutrition

Font styles to use
Sans Serif

Requirements
Must have
• 1. Follows proper Label Guidelines
2. Within Given Label Dimensions
3. Attractive & Unique Label Designs
4. Excellent Color Combinations
Nice to have
• My Product containers will a Black Color Tub. Adjust the label background color accordingly so that it looks attractive.
Should not have
• Exact Label designs for any existing products

```html
<!DOCTYPE html>
<html lang="en">
<head>
<meta charset="UTF-8">
<title>Keltravo Organic Protein – Chocolate Label</title>
<link rel="stylesheet" href="https://fonts.googleapis.com/css2?family=Montserrat:wght@500;600;700&family=Permanent+Marker&family=Russo+One&family=Oswald:wght@500;600&display=swap">
<style>
  :root {
    --page-bg: #eeeeee;
    --label-light: #fbfbfb;
    --label-mid: #e6e6e6;
    --ink-dark: #2e2e2e;
    --ink-grey: #5a5a5a;
    --organic-green: #3aa347;
    --band-dark: #262626;
    --band-panel: #3a3a3a;
    --choc-dark: #3d2219;
    --choc-mid: #5a3427;
    --circle-1: #62b846;
    --circle-2: #15a04b;
    --circle-3: #0f9a48;
    --circle-4: #4daf47;
    --circle-5: #8dba3a;
    --white: #ffffff;
  }
  * { margin: 0; padding: 0; box-sizing: border-box; }
  html, body { width: 1200px; height: 1200px; overflow: hidden; background: var(--page-bg); }
  .canvas { position: relative; width: 1200px; height: 1200px; }

  .label {
    position: absolute; left: 70px; top: 200px; width: 1060px; height: 820px;
    background: linear-gradient(90deg, var(--label-mid) 0%, var(--label-light) 30%, var(--label-light) 70%, var(--label-mid) 100%);
    overflow: hidden;
  }

  .brand-side {
    position: absolute; left: 110px; top: 300px;
    transform-origin: left top; transform: rotate(-90deg);
    display: flex; align-items: center; gap: 10px;
    font-family: "Montserrat", sans-serif; font-weight: 700; font-size: 38px; color: var(--ink-dark);
  }
  .brand-side .brand-dot { width: 14px; height: 14px; border-radius: 50%; background: var(--organic-green); }

  .title-art { position: absolute; left: 165px; top: 60px; }
  .title-organic { font-family: "Permanent Marker", sans-serif; fill: var(--organic-green); }
  .title-protein { font-family: "Russo One", sans-serif; fill: var(--ink-dark); }

  .supplement-note {
    position: absolute; left: 788px; top: 84px;
    font-family: "Montserrat", sans-serif; font-weight: 600; font-size: 17px;
    letter-spacing: 3px; line-height: 1.5; color: var(--ink-dark);
  }

  .tagline {
    position: absolute; left: 0; width: 100%; top: 320px; text-align: center;
    font-family: "Montserrat", sans-serif; font-weight: 600; font-size: 27px;
    letter-spacing: 1.5px; color: var(--ink-grey);
  }

  .benefits { position: absolute; left: 0; top: 438px; width: 1060px; height: 200px; }
  .benefit-label {
    position: absolute; top: 150px; width: 200px; text-align: center;
    font-family: "Oswald", sans-serif; font-weight: 600; font-size: 17px;
    letter-spacing: 1px; color: var(--ink-dark);
  }

  .flavor-band { position: absolute; left: 0; bottom: 0; width: 1060px; height: 142px; }
  .net-weight {
    position: absolute; left: 14px; bottom: 62px;
    font-family: "Montserrat", sans-serif; font-weight: 500; font-size: 17px;
    line-height: 1.35; color: var(--white);
  }
  .flavor-name {
    position: absolute; left: 0; width: 100%; bottom: 38px; text-align: center;
    font-family: "Montserrat", sans-serif; font-weight: 600; font-size: 28px;
    letter-spacing: 5px; line-height: 1.25; color: var(--white);
  }
  .servings {
    position: absolute; right: 14px; bottom: 70px;
    font-family: "Oswald", sans-serif; font-weight: 600; font-size: 22px; color: #bdbdbd;
  }
  .servings strong { font-size: 40px; margin-right: 6px; }
</style>
</head>
<body>
<div class="canvas">
  <section class="label">

    <div class="brand-side"><span class="brand-dot"></span><span>Keltravo</span></div>

    <svg class="title-art" width="780" height="250" viewBox="0 0 780 250" aria-label="Organic Protein">
      <text class="title-organic" x="10" y="92" font-size="92" textLength="372" lengthAdjust="spacingAndGlyphs">ORGANIC</text>
      <text class="title-protein" x="0" y="242" font-size="170" textLength="750" lengthAdjust="spacingAndGlyphs">PROTEIN</text>
    </svg>

    <div class="supplement-note">DIETARY<br>SUPPLEMENT</div>

    <p class="tagline">ALL-IN-ONE ORGANIC SHAKE</p>

    <div class="benefits">
      <svg width="1060" height="150" viewBox="0 0 1060 150">
        <circle cx="347" cy="72" r="62" fill="var(--circle-1)" role="img" aria-label="Energy icon: figure in meditation pose"/>
        <circle cx="444" cy="72" r="62" fill="var(--circle-2)"/>
        <circle cx="540" cy="72" r="62" fill="var(--circle-3)" role="img" aria-label="Endurance icon: running figure"/>
        <circle cx="636" cy="72" r="62" fill="var(--circle-4)"/>
        <circle cx="740" cy="72" r="62" fill="var(--circle-5)" role="img" aria-label="Strength icon: flexing figure"/>
      </svg>
      <span class="benefit-label" style="left:247px">ENERGY</span>
      <span class="benefit-label" style="left:440px">ENDURANCE</span>
      <span class="benefit-label" style="left:640px">STRENGHT</span>
    </div>

    <div class="flavor-band">
      <svg width="1060" height="142" viewBox="0 0 1060 142">
        <defs>
          <linearGradient id="chocGrad" x1="0" y1="0" x2="1" y2="0">
            <stop offset="0" stop-color="var(--choc-dark)"/>
            <stop offset="0.5" stop-color="var(--choc-mid)"/>
            <stop offset="1" stop-color="var(--choc-dark)"/>
          </linearGradient>
        </defs>
        <rect x="0" y="0" width="1060" height="142" fill="var(--band-dark)"/>
        <polygon points="0,0 240,0 218,142 0,142" fill="var(--band-panel)"/>
        <polygon points="820,0 1060,0 1060,142 842,142" fill="var(--band-panel)"/>
        <polygon points="262,0 798,0 820,142 240,142" fill="url(#chocGrad)"/>
        <line x1="250" y1="0" x2="228" y2="142" stroke="#9a9a9a" stroke-width="4"/>
        <line x1="810" y1="0" x2="832" y2="142" stroke="#9a9a9a" stroke-width="4"/>
      </svg>
      <div class="net-weight">NET WT. 25.0 oz<br>(1 lb 9 oz) 708g</div>
      <div class="flavor-name">CHOCOLATE<br>FLAVOR</div>
      <div class="servings"><strong>50</strong>SERVINGS</div>
    </div>

  </section>
</div>
</body>
</html>
```